VALTERRA Constructions stationery

Want following designed. Business cards. Letterhead. Email footer. A4 folder cover - front and side. Postcard. For two logo's. VALTERRA CONSTRUCTIONS and VALTERRA INTERIOR DESIGN. Logo's will be provided. Logo is black and metallic Gold.

We are a high end residential design and build company that builds for ourself and exclusive clients who we select to build for. We don't target high volume but high quality projects and build only for clients who pass a number of checks. Ultimately we choose our client and build very high end finishes in remodelling or new home builds. We have no website but will be designing one in the next month.

Target Market(s)

High end residential homes

Industry/Entity Type

Residential Construction

Font styles to use
Serif

Colors
000000
ffc214

Requirements
Must have
• Clean and simplistic. Must represent high end, sophistication, perfection and be sharp.
Nice to have
• We are a high end design and build company that is exclusive to clients we select to build for. We also add our own eclusive one off designs in each build for bathrooms and kitchens like towel rails, vanitys etc.
Should not have
• Animation or unsophisticated

```html
<!DOCTYPE html>
<html lang="en">
<head>
<meta charset="utf-8">
<title>VALTERRA Interior Design – Business Card</title>
<link rel="stylesheet" href="https://fonts.googleapis.com/css2?family=Playfair+Display:wght@700&family=Open+Sans:wght@400;600&display=swap">
<style>
  :root {
    --stage: #e9e6e1;
    --card-black: #1d1e20;
    --card-black-deep: #151617;
    --card-white: #fbfbfa;
    --ink: #111111;
    --paper-text: #f2f2f2;
    --gold: #b08d35;
    --gold-light: #d2b05a;
    --gold-dark: #7d6220;
    --serif: "Playfair Display", Georgia, serif;
    --sans: "Open Sans", Arial, sans-serif;
  }
  * { box-sizing: border-box; margin: 0; padding: 0; }
  html, body { width: 1200px; height: 911px; overflow: hidden; }
  body { background: var(--stage); font-family: var(--sans); position: relative; }

  .card {
    position: absolute;
    width: 640px;
    height: 366px;
    border-radius: 22px;
    overflow: hidden;
    box-shadow: 0 10px 28px rgba(0,0,0,.22);
  }

  /* Front side */
  .card--front { left: 60px; top: 50px; background: linear-gradient(160deg, var(--card-black) 0%, var(--card-black-deep) 100%); color: var(--paper-text); }
  .front__decoration {
    position: absolute; left: 40px; top: 150px; width: 250px; height: 200px;
    border-radius: 50%;
    background: radial-gradient(circle, #252628 0%, #202123 60%, rgba(32,33,35,0) 72%);
  }
  .brand { position: absolute; left: 70px; top: 50px; }
  .brand__name {
    font-family: var(--serif); font-weight: 700; font-size: 30px; line-height: 1.05;
    letter-spacing: 1px;
  }
  .brand__tagline { font-size: 11.5px; margin-top: 6px; letter-spacing: .2px; }
  .card--front .brand__name { color: var(--paper-text); }

  .contact { position: absolute; right: 34px; top: 104px; display: flex; gap: 14px; }
  .contact__lines { text-align: right; font-size: 14px; line-height: 1.38; }
  .contact__gap { height: 14px; }
  .contact__icons { display: flex; flex-direction: column; gap: 4px; padding-top: 46px; }
  .contact__icons svg { width: 15px; height: 15px; fill: var(--gold-light); }

  .person { position: absolute; left: 70px; bottom: 42px; }
  .person__name { color: var(--gold-light); font-size: 17px; letter-spacing: .5px; }
  .person__role { font-size: 15px; margin-top: 2px; }

  /* Back side */
  .card--back { left: 500px; top: 495px; background: var(--card-white); color: var(--ink); }
  .card--back .brand { left: 0; right: 0; top: 100px; text-align: center; }
  .card--back .brand__name { font-size: 38px; color: var(--ink); }
  .card--back .brand__tagline { font-size: 13px; color: var(--ink); margin-top: 8px; }
  .back__url {
    position: absolute; left: 0; right: 0; bottom: 52px; text-align: center;
    font-size: 12px; letter-spacing: 7px; color: var(--gold);
  }
  .back__band {
    position: absolute; left: 0; right: 0; bottom: 20px; height: 22px;
    background: linear-gradient(90deg, var(--gold-dark), var(--gold-light) 50%, var(--gold-dark));
  }
</style>
</head>
<body>

  <section class="card card--front">
    <div class="front__decoration" role="img" aria-label="Faint large floral emblem decoration"></div>

    <div class="brand">
      <div class="brand__name">VALTERRA<br>INTERIOR DESIGN</div>
      <div class="brand__tagline">Interior Architecture · Space design · Staging</div>
    </div>

    <div class="contact">
      <div class="contact__lines">
        <div>1420 Harbour Crest Road</div>
        <div>Dunmore Bay, Westmere 60218</div>
        <div class="contact__gap"></div>
        <div>555 210 4471</div>
        <div>555 386 2907</div>
        <div>555 742 1638</div>
        <div>studio@valterra-id.com</div>
        <div>www.valterra-id.com</div>
      </div>
      <div class="contact__icons">
        <svg viewBox="0 0 16 16" aria-label="Phone"><path d="M4 1l3 3-2 2c1 2 3 4 5 5l2-2 3 3-2 3C7 15 1 9 1 3z"/></svg>
        <svg viewBox="0 0 16 16" aria-label="Mobile"><path d="M4 0h8v16H4zM5.5 2v10h5V2z"/></svg>
        <svg viewBox="0 0 16 16" aria-label="Fax"><path d="M4 1h8v4H4zM1 6h14v7H1zM4 10h8v5H4z"/></svg>
        <svg viewBox="0 0 16 16" aria-label="Email"><path d="M1 3h14v10H1zM2 4l6 5 6-5z" fill-rule="evenodd"/></svg>
        <svg viewBox="0 0 16 16" aria-label="Website"><circle cx="8" cy="8" r="7"/></svg>
      </div>
    </div>

    <div class="person">
      <div class="person__name">ELIAS MARLOW</div>
      <div class="person__role">CEO/FOUNDER</div>
    </div>
  </section>

  <section class="card card--back">
    <div class="brand">
      <div class="brand__name">VALTERRA<br>INTERIOR DESIGN</div>
      <div class="brand__tagline">Interior Architecture · Space design · Staging</div>
    </div>
    <div class="back__url">www.valterra-id.com</div>
    <div class="back__band"></div>
  </section>

</body>
</html>
```